Shine Crew

I need a flyer and business cards to hand out at office buildings and country clubs introducing my new auto detailing business, SHINE CREW. Call or text 913-555-0147 for an appointment. Complete auto detailing done at their place or mine, and we offer pick -up and drop-off, if needed. I believe the flyer needs a car on it. Black, blue, and pink are my preferred colors. While you go about your day's business, whether playing 18 holes of golf or putting in 8 hours at the office, we will have your ride shining like a new penny when you're ready to roll!

```html
<!DOCTYPE html>
<html lang="en">
<head>
<meta charset="utf-8">
<title>Shine Crew – Flyer and Business Cards</title>
<link href="https://fonts.googleapis.com/css2?family=Raleway:wght@300;400;500;600;700;800&family=Outfit:wght@400;500&display=swap" rel="stylesheet">
<style>
  :root {
    --ink: #1b1b20;
    --white: #ffffff;
    --red: #ee1c24;
    --red-deep: #c4192b;
    --purple: #5a2a78;
    --blue: #16309a;
    --blue-band: #13309b;
    --grey-light: #f2f2f2;
    --grey-mid: #cfcfcf;
    --grey-soft: #c9c9cc;
    --text-dark: #111114;
  }
  * { box-sizing: border-box; margin: 0; padding: 0; }
  html, body { width: 783px; height: 1200px; overflow: hidden; background: var(--white); }
  body { position: relative; font-family: "Raleway", sans-serif; color: var(--white); }

  /* ---------- Wordmark ---------- */
  .brand-name { position: absolute; left: 0; width: 100%; text-align: center; font-family: "Outfit", sans-serif; font-weight: 500; color: var(--white); white-space: nowrap; }

  /* ---------- Flyer ---------- */
  .flyer { position: absolute; left: 81px; top: 70px; width: 621px; height: 800px; background: var(--ink); overflow: hidden; }

  .flyer-header { position: absolute; left: 0; top: 0; width: 621px; height: 152px; }
  .flyer-header .brand-name { width: 258px; top: 58px; font-size: 32px; line-height: 40px; }
  .headline { position: absolute; left: 273px; top: 20px; font-family: "Outfit", sans-serif; font-weight: 400; font-size: 28px; line-height: 32px; white-space: nowrap; }
  .headline .accent { color: var(--red); font-weight: 500; }
  .intro { position: absolute; left: 273px; top: 91px; width: 332px; font-size: 10.3px; line-height: 11.8px; font-weight: 400; }

  .reach-band { position: absolute; left: 0; top: 152px; width: 621px; height: 37px; background: var(--blue-band); display: flex; align-items: center; justify-content: center; font-family: "Outfit", sans-serif; font-size: 19px; white-space: nowrap; }

  .hero { position: absolute; left: 0; top: 189px; width: 621px; height: 337px; }
  .hero-photo { position: absolute; inset: 0; background: radial-gradient(ellipse at 75% 30%, #8e1c22 0%, #4a1418 40%, transparent 70%), linear-gradient(160deg, #2a2a30 0%, #1a0e10 45%, #6d1519 80%, #3b0a0d 100%); }
  .pickup-card { position: absolute; left: 28px; top: 0; width: 213px; height: 135px; border-radius: 0 0 20px 20px; background: linear-gradient(135deg, var(--red-deep) 0%, #a11f45 40%, var(--purple) 100%); box-shadow: 0 4px 10px rgba(0,0,0,0.45); text-align: center; padding-top: 12px; }
  .pickup-title { font-family: "Outfit", sans-serif; font-weight: 500; font-size: 20.5px; line-height: 23.5px; }
  .pickup-text { font-weight: 700; font-size: 9.6px; line-height: 12px; margin-top: 5px; white-space: nowrap; }
  .detail-inset { position: absolute; left: 424px; top: 136px; width: 174px; height: 174px; border-radius: 50%; padding: 3px; background: linear-gradient(200deg, var(--red) 0%, var(--purple) 60%, var(--blue) 100%); }
  .detail-inset-photo { width: 100%; height: 100%; border-radius: 50%; background: radial-gradient(circle at 45% 40%, #b5b9bf 0%, #6f747c 45%, #2c2e33 100%); }

  .services-band { position: absolute; left: 0; top: 526px; width: 621px; height: 37px; background: linear-gradient(90deg, var(--red) 0%, #8b2355 50%, var(--blue) 100%); display: flex; align-items: center; justify-content: center; font-weight: 700; font-size: 11.8px; white-space: nowrap; gap: 10px; }

  .booking { position: absolute; left: 0; top: 563px; width: 621px; height: 185px; background: linear-gradient(90deg, var(--grey-mid) 0%, var(--grey-light) 35%, var(--white) 70%, var(--grey-mid) 100%); color: var(--text-dark); text-align: center; }
  .booking-call { position: absolute; left: 0; width: 621px; top: 24px; font-weight: 500; font-size: 21.5px; line-height: 26px; white-space: nowrap; }
  .booking-call .phone { font-weight: 600; font-size: 29px; }
  .hours-pill { position: absolute; left: 186px; top: 90px; width: 250px; height: 29px; border-radius: 8px; background: linear-gradient(90deg, var(--blue) 0%, #6a2668 55%, var(--red) 100%); color: var(--white); font-family: "Outfit", sans-serif; font-size: 12.5px; display: flex; align-items: center; justify-content: center; }
  .service-areas { position: absolute; left: 0; width: 621px; top: 131px; font-size: 12px; line-height: 15px; font-weight: 500; }

  .flyer-footer { position: absolute; left: 0; top: 748px; width: 621px; height: 52px; display: flex; align-items: center; text-transform: uppercase; white-space: nowrap; }
  .footer-promise { position: absolute; left: 38px; color: var(--red); font-weight: 700; font-size: 11.8px; }
  .footer-tagline { position: absolute; left: 305px; font-weight: 500; font-size: 9.9px; }

  /* ---------- Business cards ---------- */
  .card { position: absolute; top: 914px; width: 282px; height: 176px; background: var(--ink); overflow: hidden; }
  .card-front { left: 93px; }
  .card-back { left: 415px; }
  .card-front .brand-name { top: 72px; font-size: 22px; line-height: 28px; }
  .card-banner { position: absolute; left: 0; top: 128px; width: 282px; height: 19px; background: linear-gradient(90deg, var(--blue) 0%, #7a2460 50%, var(--red) 100%); display: flex; align-items: center; justify-content: center; font-size: 10.9px; font-weight: 400; white-space: nowrap; }
  .card-back .brand-name { top: 70px; font-size: 17px; line-height: 22px; }
  .contact-name { position: absolute; left: 48px; top: 114px; font-size: 12px; font-weight: 300; white-space: nowrap; }
  .contact-name strong { font-weight: 500; }
  .contact-role { position: absolute; left: 48px; top: 132px; font-size: 6.5px; font-weight: 400; color: var(--grey-soft); }
  .contact-divider { position: absolute; left: 141px; top: 115px; width: 1px; height: 35px; background: var(--red-deep); }
  .contact-line { position: absolute; left: 152px; display: flex; align-items: center; gap: 5px; white-space: nowrap; }
  .contact-phone { top: 116px; font-size: 11px; font-weight: 600; }
  .contact-address { top: 136px; font-size: 4.6px; font-weight: 700; line-height: 6.5px; }
  .contact-line svg { flex: none; }
</style>
</head>
<body>

<section class="flyer">
  <header class="flyer-header">
    <div class="brand-name">Shine Crew</div>
    <h1 class="headline">Transform Your Ride with<br><span class="accent">Shine Crew!</span></h1>
    <p class="intro">Looking for a sparkling clean car without the hassle? Whether you're hitting the golf course or putting in a full day at the office, Shine Crew brings the shine to you. We offer premium mobile auto detailing at your convenience.</p>
  </header>

  <div class="reach-band">We come to you, Whether at the office, country club, or your home!</div>

  <div class="hero">
    <div class="hero-photo" role="img" aria-label="Photo of a detailer in a red shirt and white gloves polishing the hood of a glossy red car"></div>
    <div class="pickup-card">
      <div class="pickup-title">We also offer<br>pick-up and<br>drop-off services</div>
      <p class="pickup-text">if needed. No need to interrupt your day,<br>we'll handle the details while you focus<br>on what matters to you.</p>
    </div>
    <div class="detail-inset">
      <div class="detail-inset-photo" role="img" aria-label="Close-up photo of a hand wiping a car dashboard console with a microfiber cloth"></div>
    </div>
  </div>

  <div class="services-band"><span>Our Services Include:&nbsp; Complete Interior &amp; Exterior Detailing</span><span>|</span><span>Hand wash, wax, tire shine &amp; more!</span></div>

  <div class="booking">
    <p class="booking-call">Call or text us at: <span class="phone">913-555-0147</span><br>to schedule your appointment today!</p>
    <div class="hours-pill">Flexible hours – by appointment only</div>
    <p class="service-areas">Service Areas:<br>Your area, or "Office buildings &amp; country clubs across the area"</p>
  </div>

  <footer class="flyer-footer">
    <span class="footer-promise">Flexible hours. Personalized service.</span>
    <span class="footer-tagline">Let us do the dirty work while you enjoy your day!</span>
  </footer>
</section>

<section class="card card-front">
  <div class="brand-name">Shine Crew</div>
  <div class="card-banner">TRANSFORM YOUR RIDE WITH SHINE CREW!</div>
</section>

<section class="card card-back">
  <div class="brand-name">Shine Crew</div>
  <div class="contact-name">Jordan <strong>Reyes</strong></div>
  <div class="contact-role">Director</div>
  <div class="contact-divider"></div>
  <div class="contact-line contact-phone">
    <svg width="8" height="8" viewBox="0 0 24 24" aria-hidden="true"><path fill="#6a3fa0" d="M6.6 10.8a15.1 15.1 0 0 0 6.6 6.6l2.2-2.2a1 1 0 0 1 1-.25 11.4 11.4 0 0 0 3.6.57 1 1 0 0 1 1 1V20a1 1 0 0 1-1 1A17 17 0 0 1 3 4a1 1 0 0 1 1-1h3.5a1 1 0 0 1 1 1c0 1.25.2 2.45.57 3.6a1 1 0 0 1-.25 1z"/></svg>
    <span>913-555-0147</span>
  </div>
  <div class="contact-line contact-address">
    <svg width="7" height="9" viewBox="0 0 24 30" aria-hidden="true"><path fill="none" stroke="#c4192b" stroke-width="3" d="M12 28s9-9.5 9-16a9 9 0 0 0-18 0c0 6.5 9 16 9 16z"/><circle cx="12" cy="12" r="3" fill="#c4192b"/></svg>
    <span>YOUR CITY ADDRESS<br>STREET LOCATION, NY CITY, USA</span>
  </div>
</section>

</body>
</html>
```